Webdesign für Frauen-Personal-Training
Sehr schnelle Umsetzung meiner Wünsche und Ideen
Zielgruppe
Personal Training für Frauen in Führungspositionen ab 30 Jahren
Aufgabenstellung
Bilderwelt stimmig, Farbfokus auf CI Farben (im Anhang wie auch Logo), 1/3 Text, 2/3 Bilderwelt
- Hamburger Menü, kein klassisches
- Footer: Anschrift, Datenschutz, Impressum
- Headerimage mit Seitentitel im Bild, Titelunterschrift 2/3 der Bildschirmhöhe
- Berücksichtigung von Whitespace
- Verwendung von Icons zum Beispiel auf der Startseite beim Punkt 'du suchst - ich biete'
Seiten:
- Startseite: Einstieg für Besucher der Homepage in der Richtung 'du suchst, ich biete', abschließend Formular --> Abschluss Kontaktformular
- Training: Trainingsweise und Arbeitsweise beschreiben
- Über mich (Aufbau der Seite gleich wie 'Training' und 'Preise'): Professionelle Erfahrungen in Richtung training, Ernährung, Gesundheit --> Abschluss: CTA 'Nimm Kontakt zu mir auf und informiere dich in einem persönlichen Gespräch --> Link auf Kontaktseite
- Räumlichkeiten --> Abschluss: CTA 'Nimm Kontakt zu mir auf und informiere dich in einem persönlichen Gespräch --> Link auf Kontaktseite
- Preise --> Abschluss: CTA 'Nimm Kontakt zu mir auf und informiere dich in einem persönlichen Gespräch --> Link auf Kontaktseite
- Kontaktseite (Landing Page)
(- Impressum / Datenschutzseite)
Beispielseite:
https://www.quintello.com/rastavoni

```html
<!DOCTYPE html>
<html lang="de">
<head>
<meta charset="utf-8">
<title>Über mich – Formwerk</title>
<link rel="stylesheet" href="https://fonts.googleapis.com/css2?family=Titillium+Web:wght@400;600&family=Rubik:wght@400;500&display=swap">
<style>
:root{
  --olive:#7b7560;
  --green:#679e7a;
  --brand:#3aa57a;
  --ink:#222222;
  --body:#444444;
  --track:#e9e9e9;
  --footer:#282622;
  --white:#ffffff;
}
*{margin:0;padding:0;box-sizing:border-box}
html,body{width:1200px;height:2204px;overflow:hidden;background:var(--white)}
body{position:relative;font-family:"Rubik",sans-serif;color:var(--body)}
.abs{position:absolute}
.heading{font-family:"Titillium Web",sans-serif;font-weight:400;color:var(--ink)}

.header-band{left:484px;top:0;width:716px;height:325px;background:var(--olive)}
.brand{left:93px;top:18px;display:flex;flex-direction:column}
.brand-name{font-family:"Rubik",sans-serif;font-weight:500;font-size:20px;color:var(--brand);line-height:1}
.brand-tag{font-size:8px;color:var(--ink);margin-top:3px;padding-left:2px}
.menu-toggle{left:1076px;top:27px;width:29px;height:10px;border-top:2px solid var(--white);border-bottom:2px solid var(--white)}

.hero{left:93px;top:62px;width:1013px;height:200px;background:linear-gradient(90deg,#eeeeed 0%,#f3f1ee 45%,#d8d2cc 70%,#ece9e6 100%)}
.hero-title{left:232px;top:134px;font-size:40px;line-height:1.2}

.rule{left:233px;top:410px;width:61px;height:3px;background:var(--green)}
.story-title{left:232px;top:472px;font-size:39px;line-height:40px}
.story-text{left:422px;top:594px;width:545px;font-size:11px;line-height:22.5px}

.quote-band{left:0;top:835px;width:715px;height:312px;background:var(--green)}
.team-photo{left:483px;top:772px;width:482px;height:312px;background:linear-gradient(110deg,#e7e4df 0%,#f4f4f2 45%,#d9dde0 70%,#4b5a78 100%)}
.quote-mark{left:234px;top:878px;font-family:"Titillium Web",sans-serif;font-weight:600;font-style:italic;font-size:36px;line-height:1;color:var(--white)}
.quote-text{left:234px;top:911px;width:205px;font-family:"Titillium Web",sans-serif;font-size:14.5px;line-height:30px;color:var(--white)}
.quote-author{left:234px;top:1075px;display:flex;align-items:center;gap:12px;font-size:10.5px;color:var(--white)}
.quote-author::before{content:"";width:44px;height:1px;background:var(--white)}

.choose-title{left:233px;top:1202px;font-size:22px}
.choose-text{left:233px;top:1260px;width:360px;font-size:11px;line-height:22.5px}
.skill{left:670px;width:295px}
.skill-row{display:flex;justify-content:space-between;font-size:10.5px;color:var(--ink);text-transform:uppercase}
.skill-row span:last-child{color:#777}
.skill-track{margin-top:9px;margin-left:2px;height:3px;background:var(--track)}
.skill-fill{height:3px;background:var(--green)}

.cta-button{left:234px;top:1460px;width:216px;height:40px;background:var(--green);color:var(--white);font-family:"Titillium Web",sans-serif;font-weight:600;font-size:12.5px;letter-spacing:1.6px;display:flex;align-items:center;justify-content:center}

.portrait{left:234px;top:1625px;width:481px;height:338px;background:linear-gradient(90deg,#f2f2f2 0%,#eceae6 40%,#3e5174 60%,#f0f0ee 100%)}
.profile{left:734px;font-size:11px;color:var(--ink)}
.profile-icon{left:952px;top:1740px;width:12px;height:12px;background:var(--ink)}
.contact-card{left:672px;top:1802px;width:293px;height:211px;background:var(--green);padding:32px 27px}
.contact-text{font-size:18px;line-height:30px;color:var(--white)}
.contact-arrow{left:888px;top:1968px}

.footer{left:0;top:2141px;width:1200px;height:63px;background:var(--footer);color:var(--white);font-size:8.5px}
.footer-links{position:absolute;left:233px;top:27px;display:flex;gap:29px;font-weight:500;letter-spacing:1px}
.footer-copy{position:absolute;right:235px;top:27px}
</style>
</head>
<body>
<div class="abs header-band"></div>
<div class="abs brand"><span class="brand-name">Formwerk</span><span class="brand-tag">Personal Training für Frauen</span></div>
<div class="abs menu-toggle" aria-label="Menü"></div>

<div class="abs hero" role="img" aria-label="Hände beim Schreiben in ein Notizbuch am Schreibtisch"></div>
<h1 class="abs heading hero-title">Über mich</h1>

<div class="abs rule"></div>
<h2 class="abs heading story-title">Meine persönliche<br>Geschichte</h2>
<p class="abs story-text">Ich möchte ein wenig über meine persönliche Geschichte erzählen, die mich dazu veranlasste, Frauen zu helfen, „mutig zu sein“ und einen wahren Durchbruch zu erzielen, um ihr höchstes und bestes Potenzial und ihre aufregendsten Visionen für ihr Leben und ihre Arbeit zu erreichen. Als ich mich 40 Jahren näherte, begannen sich die Dinge zu ändern. Ich war äußerlich sehr "erfolgreich", aber innerlich kämpfte ich tief. Die meiste Zeit fühlte sich meine Arbeit falsch und unecht an, und die Vereinbarkeit von Beruf und Familie war unerreichbar. Ich konnte nicht wahrheitsgemäß sprechen oder mein wahres Selbst sein.</p>

<div class="abs quote-band"></div>
<div class="abs team-photo" role="img" aria-label="Zwei lachende Frauen im Gespräch im Büro"></div>
<div class="abs quote-mark">"</div>
<p class="abs quote-text">Mit unseren Spezialisten und Experten, die Ihnen zur Verfü-gung stehen, werden Sie kom-plexe Probleme mit Zuversicht angehen</p>
<div class="abs quote-author">Mara Lenz</div>

<h2 class="abs heading choose-title">Uns wählen</h2>
<p class="abs choose-text">Als ich mich 40 Jahren näherte, begannen sich die Dinge zu ändern. Ich war äußerlich sehr "erfolgreich", aber innerlich kämpfte ich tief. Die meiste Zeit fühlte sich meine Arbeit falsch und unecht an, und die Vereinbarkeit von Beruf und Familie war unerreichbar. Ich konnte nicht wahrheitsgemäß sprechen oder mein wahres Selbst sein.&nbsp; Ich möchte ein wenig über meine persönliche Geschichte erzählen, die mich dazu veranlasste,</p>

<div class="abs skill" style="top:1267px"><div class="skill-row"><span>Talentübernahme</span><span>93%</span></div><div class="skill-track"><div class="skill-fill" style="width:91%"></div></div></div>
<div class="abs skill" style="top:1317px"><div class="skill-row"><span>Corporate Ethics Program</span><span>95%</span></div><div class="skill-track"><div class="skill-fill" style="width:93%"></div></div></div>
<div class="abs skill" style="top:1366px"><div class="skill-row"><span>Vergütungsberatung</span><span>87%</span></div><div class="skill-track"><div class="skill-fill" style="width:86%"></div></div></div>

<a class="abs cta-button">NIMM KONTAKT ZU MIR</a>

<div class="abs portrait" role="img" aria-label="Porträt der Trainerin mit verschränkten Armen im Büro"></div>
<div class="abs profile" style="top:1673px">Jana Roth</div>
<div class="abs profile" style="top:1696px">Gründer</div>
<div class="abs profile" style="top:1741px">Berlin 2019</div>
<div class="abs profile-icon" aria-label="Profil"></div>
<div class="abs contact-card"><p class="contact-text">Nimm Kontakt zu mir auf und informiere dich in einem persönlichen Gespräch</p></div>
<svg class="abs contact-arrow" width="50" height="8" viewBox="0 0 50 8"><line x1="0" y1="4" x2="46" y2="4" stroke="#fff" stroke-width="1"/><path d="M44 1.5 L49 4 L44 6.5Z" fill="#fff"/></svg>

<footer class="abs footer">
  <div class="footer-links"><span>IMPRESSUM</span><span>DATENSCHUTZSEITE</span></div>
  <div class="footer-copy">© Formwerk 2019</div>
</footer>
</body>
</html>
```